Flyer for the Lumen 2025 Conference

I am looking to produce a flyer for our upcoming conference, Lumen 2025. This is an annual conference that we plan to publicize on social media. The ideal designer will create a flyer that is eye-catching and effectively communicates the key information. Please see attached our logo, speaker photo, and flyer content.

Target Market(s)

All demographics

Industry/Entity Type

Christian

Font styles to use
Sans Serif

Requirements
Should not have
• Cross, church

```html
<!DOCTYPE html>
<html lang="en">
<head>
<meta charset="utf-8">
<title>Lumen 2025 Conference Flyer</title>
<link rel="stylesheet" href="https://fonts.googleapis.com/css2?family=Cinzel:wght@700&family=Oswald:wght@600&family=Great+Vibes&family=Merriweather:wght@700&family=Open+Sans:ital,wght@0,400;0,600;0,700;0,800;1,700&display=swap">
<style>
  :root {
    --stage: #e7e7e9;
    --navy-deep: #070b1c;
    --navy: #0f1d3a;
    --brand-blue: #0d3a6b;
    --band-blue: rgba(14, 62, 112, 0.82);
    --gold: #f4b81d;
    --gold-light: #fff0b0;
    --gold-mid: #e0b440;
    --gold-dark: #8c6414;
    --flame: #f28a1c;
    --white: #ffffff;
    --text-navy: #143a66;
  }
  * { box-sizing: border-box; margin: 0; padding: 0; }
  html, body { width: 1200px; height: 813px; overflow: hidden; }
  body {
    background: var(--stage);
    position: relative;
    font-family: "Open Sans", Arial, sans-serif;
  }
  .flyer {
    position: absolute;
    left: 312px; top: 0;
    width: 575px; height: 813px;
    overflow: hidden;
    background:
      radial-gradient(ellipse 60% 30% at 50% 22%, rgba(214, 160, 80, 0.55), rgba(120, 90, 60, 0.18) 60%, transparent 80%),
      linear-gradient(180deg, #1a1f33 0%, #141a30 30%, var(--navy) 60%, var(--navy-deep) 100%);
  }
  .glow-band {
    position: absolute;
    left: 0; right: 0; top: 330px; height: 110px;
    background: radial-gradient(ellipse 55% 40% at 50% 50%, rgba(255, 236, 170, 0.85), rgba(230, 190, 90, 0.35) 55%, transparent 80%);
  }
  .brand-tab {
    position: absolute;
    left: 189px; top: 0;
    width: 198px; height: 118px;
    background: var(--brand-blue);
    border-radius: 0 0 12px 12px;
    display: flex; align-items: center; justify-content: center; gap: 8px;
    padding-top: 10px;
  }
  .brand-mark { width: 12px; height: 12px; border-radius: 50%; background: var(--flame); }
  .brand-name {
    font-family: "Open Sans", Arial, sans-serif;
    font-weight: 600;
    font-size: 30px;
    letter-spacing: 1px;
    color: var(--white);
  }
  .gold-text {
    background: linear-gradient(180deg, var(--gold-light) 0%, var(--gold-mid) 45%, var(--gold-dark) 100%);
    -webkit-background-clip: text; background-clip: text;
    color: transparent;
  }
  .event-title {
    position: absolute; top: 126px; left: 0; right: 0;
    text-align: center;
    font-family: "Cinzel", "Times New Roman", serif;
    font-weight: 700; font-size: 46px; letter-spacing: 1px;
  }
  .event-subtitle {
    position: absolute; top: 172px; left: 0; right: 0;
    text-align: center;
    font-family: "Great Vibes", cursive;
    font-size: 30px; color: var(--white);
  }
  .event-headline {
    position: absolute; top: 210px; left: 0; right: 0;
    text-align: center;
    font-family: "Oswald", "Arial Narrow", sans-serif;
    font-weight: 600; font-size: 48px; letter-spacing: 0.5px;
  }
  .speaker-photo {
    position: absolute;
    left: 134px; top: 266px;
    width: 274px; height: 420px;
    border-radius: 120px 120px 0 0;
    background: linear-gradient(180deg, rgba(120, 90, 70, 0.55) 0%, rgba(30, 80, 170, 0.75) 45%, rgba(20, 50, 120, 0.5) 85%, transparent 100%);
  }
  .speaker-name {
    position: absolute; top: 520px; left: 0; right: 0;
    text-align: center;
    font-weight: 800; font-size: 33px; color: var(--gold);
  }
  .speaker-role {
    position: absolute; top: 560px; left: 0; right: 0;
    text-align: center;
    font-family: "Merriweather", Georgia, serif;
    font-weight: 700; font-size: 24px; color: var(--white);
  }
  .theme-label {
    position: absolute; top: 606px; left: 0; right: 0;
    text-align: center;
    font-size: 18px; color: var(--white);
  }
  .theme-title {
    position: absolute; top: 633px; left: 0; right: 0;
    text-align: center;
    font-weight: 700; font-size: 23px; color: var(--gold);
  }
  .details-band {
    position: absolute;
    left: 8px; right: 0; top: 669px; height: 62px;
    background: linear-gradient(90deg, transparent 0%, var(--band-blue) 8%, var(--band-blue) 92%, transparent 100%);
    display: flex; flex-direction: column; align-items: center; justify-content: center; gap: 1px;
  }
  .details-line {
    font-style: italic; font-weight: 700; font-size: 17.5px; color: var(--white);
  }
  .register-button {
    position: absolute;
    left: 219px; top: 747px;
    width: 138px; height: 28px;
    background: var(--white);
    border-radius: 5px;
    display: flex; align-items: center; justify-content: center;
    font-size: 14px; font-weight: 400; color: var(--text-navy);
  }
  .website {
    position: absolute; top: 777px; left: 0; right: 0;
    text-align: center;
    font-size: 16px; color: var(--white);
  }
</style>
</head>
<body>
  <main class="flyer">
    <div class="glow-band"></div>

    <header class="brand-tab">
      <span class="brand-mark"></span>
      <span class="brand-name">NORIVA</span>
    </header>

    <h1 class="event-title gold-text">LUMEN 2025</h1>
    <p class="event-subtitle">A Prophetic Conference</p>
    <h2 class="event-headline gold-text">THE VOICE OF THE LORD</h2>

    <div class="speaker-photo" role="img" aria-label="Portrait photo of the lead speaker in a blue blazer, glasses and grey knit sweater"></div>

    <p class="speaker-name">PASTOR DANIEL MARO</p>
    <p class="speaker-role">Lead Speaker</p>

    <p class="theme-label">THEME:</p>
    <p class="theme-title">UNVEILING THE FUTURE</p>

    <section class="details-band">
      <p class="details-line">Dates: October 26-29, 2025</p>
      <p class="details-line">Venue: City Convention Center</p>
    </section>

    <div class="register-button">REGISTER NOW!</div>
    <p class="website">www.lumen2025.org</p>
  </main>
</body>
</html>
```